Style Template created - Report Accounting and Advisory industry

We need a style template created to set out a report for advice. The report follows <br/><br/>- Cover Page - ( we would need to print to a letter head )<br/>- General Disclaimer<br/>- Space to add Excel Reports in to the document- Maybe inserted Pdf's later<br/>- Action Plan dot points under headings<br/>- List of Strategies to be adopted<br/><br/>Attached is a quick example word doc that needs Custom Style Templates made so that we can quickly format items added. Also the ugly PDF that we currently produce for clients <br/><br/>Red - is our preferred Colour<br/><br/>

Target Market(s)

Accounting / Business / Professionals

Industry/Entity Type

Accounting

Colors
ec1f27

Requirements
Nice to have
• Simple Clean design. Not to busy. Easy to modify the "wording text" in design
Should not have
• Too busy or too much color

```html
<!DOCTYPE html>
<html lang="en">
<head>
<meta charset="utf-8">
<title>Tax Planning Report – Style Template</title>
<link rel="stylesheet" href="https://fonts.googleapis.com/css2?family=Lato:wght@300;400;700&display=swap">
<style>
  :root {
    --brand-red: #ec1f27;
    --ink: #3a3a3a;
    --ink-soft: #6b6b6b;
    --band: #dcd8d1;
    --rule: #e6e3de;
    --divider-page: #e2dfda;
    --canvas: #ffffff;
  }
  * { box-sizing: border-box; margin: 0; padding: 0; }
  html, body {
    width: 1200px; height: 588px; overflow: hidden;
    background: var(--canvas);
    font-family: "Lato", Arial, sans-serif;
    color: var(--ink);
  }
  .spread { position: relative; width: 1200px; height: 588px; }

  .sheet {
    position: absolute;
    width: 327px; height: 462px;
    padding: 0 23px;
    background: #fff;
    transform: scale(.469);
    transform-origin: 0 0;
    box-shadow: 0 1px 4px rgba(0,0,0,.28);
    overflow: hidden;
  }
  .sheet--divider { background: var(--divider-page); }

  .running-head {
    position: absolute; top: 11px; right: 23px;
    font-size: 3.6px; color: var(--ink-soft);
  }
  .band {
    position: absolute; top: 24px; left: 23px; right: 23px;
    height: 6px; background: var(--band);
  }
  .sheet--divider .band { background: #cfcac2; }
  .page-title {
    position: absolute; top: 36px; left: 23px;
    font-size: 11.5px; font-weight: 400; color: #222;
  }
  .body { position: absolute; left: 23px; right: 23px; }
  .body p, .body li { font-size: 4px; line-height: 1.85; color: var(--ink-soft); }
  .body p + p { margin-top: 4px; }
  .body ul { list-style: none; margin-top: 1px; }
  .body li { padding-left: 9px; position: relative; }
  .body li::before { content: "•"; position: absolute; left: 1px; }

  /* cover */
  .cover-brand {
    position: absolute; top: 22px; left: 22px;
    font-size: 15px; font-weight: 400; color: var(--brand-red);
    letter-spacing: .3px; text-transform: uppercase;
  }
  .cover-brand small {
    display: block; font-size: 3.6px; color: var(--ink-soft);
    letter-spacing: .4px; margin-top: 1px;
  }
  .cover-mark {
    position: absolute; top: 18px; right: 20px;
    width: 46px; height: 46px; border-radius: 50%;
    background: var(--brand-red);
  }
  .cover-title {
    position: absolute; top: 160px; right: 24px; text-align: right;
    font-size: 20px; font-weight: 300; line-height: 1.25; color: #555;
  }
  .cover-client {
    position: absolute; top: 230px; right: 24px;
    font-size: 6.5px; color: #444;
  }
  .cover-rule {
    position: absolute; top: 410px; left: 23px; right: 23px;
    height: 1px; background: var(--brand-red);
  }
  .cover-footer { position: absolute; top: 420px; left: 23px; }
  .cover-footer p { font-size: 3.5px; line-height: 1.9; color: #444; }
  .cover-footer .accent { color: var(--brand-red); }

  /* purpose page */
  .lead { font-size: 5px !important; color: #333 !important; }
  .pull-quote {
    font-size: 11px; font-weight: 700; line-height: 1.45;
    letter-spacing: .6px; color: var(--brand-red); text-transform: uppercase;
  }
  .section-head { font-size: 7px; color: var(--brand-red); font-weight: 400; margin-bottom: 1px; }
  .sign-off p { color: var(--brand-red) !important; }

  /* action plan */
  .action-block {
    position: absolute; left: 23px; right: 23px;
    border-top: 1px solid var(--rule); padding-top: 5px;
    font-size: 3.6px; color: #333;
  }

  /* divider page */
  .divider-title {
    position: absolute; top: 36px; left: 23px;
    font-size: 14.5px; font-weight: 400; line-height: 1.45; color: #222;
  }

  /* strategies */
  .sub-title { font-size: 11.5px; color: #222; font-weight: 400; }
  .strat { border-top: 1px solid var(--rule); padding-top: 6px; margin-top: 9px; }
  .strat h3 { font-size: 4.3px; font-weight: 700; color: var(--brand-red); margin-bottom: 4px; }
  .strat h4 { font-size: 4px; font-weight: 700; color: #333; text-transform: uppercase; margin: 4px 0 2px; }
  .note { font-style: italic; }
  .term { color: #333; font-weight: 700; }
</style>
</head>
<body>
<main class="spread">

  <!-- Row 1 -->
  <section class="sheet sheet--cover" style="left:77px; top:72px;">
    <div class="cover-brand">Hartwell Lane<small>CHARTERED ACCOUNTANTS</small></div>
    <div class="cover-mark" aria-hidden="true"></div>
    <h1 class="cover-title">Taxation Projection<br>and Planning 2020</h1>
    <p class="cover-client">Client Name</p>
    <div class="cover-rule"></div>
    <div class="cover-footer">
      <p><span class="accent">Meridale Pty Ltd</span> ACN 000 000 000</p>
      <p>12 Harbour Street, Eastfield WA 6000 &nbsp;|&nbsp; Tel: (08) 9000 0000</p>
      <p class="accent">Director Dana Hartwell B Bus CA</p>
      <p>Liability limited by a scheme approved under Professional Standards Legislation</p>
    </div>
  </section>

  <section class="sheet" style="left:253px; top:72px;">
    <span class="running-head">2020 Tax Planning | Client Name Here</span>
    <div class="band"></div>
    <h2 class="page-title">Purpose of Tax Planning</h2>
    <div class="body" style="top:62px;"><p class="lead">Why bother.....???</p></div>
    <div class="body" style="top:108px;">
      <p>Tax planning is the activities taken to minimise tax liabilities to ensure all available allowances, deductions, exclusions and exemptions are working together in the most tax effective manner to reduce the total tax bill.</p>
      <p>The purpose of this report is to provide a recommendation of strategies for you to consider for the year to come. This report is not intended to be our final advice to you, but instead a starting point in educating you on potential opportunities.</p>
      <p>Tax planning strategies are typically employed to help a business achieve their financial and business goals. The benefits of tax planning are:</p>
      <ul>
        <li>Lowering the amount of taxable income</li>
        <li>Reducing the tax rate</li>
        <li>Allowing greater control of when taxes get paid</li>
        <li>Better management of your cashflow</li>
        <li>Eliminating nasty tax surprises</li>
      </ul>
    </div>
    <div class="body" style="top:244px;">
      <p class="pull-quote">“If you fail to plan, you are<br>planning to fail”</p>
    </div>
    <div class="body" style="top:300px;">
      <h3 class="section-head">Recommendation</h3>
      <p>We will provide you with a list of action plans and a further list of items. The list will be broken down in short term and longer term action. Also a list of actions to follow up on and work on this year.</p>
      <h3 class="section-head" style="margin-top:5px;">Basis of Preparation</h3>
      <p>The taxation estimate has been prepared on the basis of information provided by the client. The report is intended for internal tax planning purposes and represents a "what if scenario". It does not necessarily represent real or intended transactions. HartwellLane have not performed any tests to verify or validate any of the information provided by the client and accordingly express no assurance as to the outcome indicated.</p>
      <p>To the extent permitted by law we do not accept liability for any loss or damage which any person, other than the client, may suffer arising from any negligence on our part. No person should rely on the taxation estimate without having a full review or audit conducted on the data.</p>
    </div>
  </section>

  <section class="sheet" style="left:429px; top:72px;">
    <span class="running-head">2020 Tax Planning | Client Name Here</span>
    <div class="band"></div>
    <h2 class="page-title">Superannuation</h2>
    <div class="body" style="top:108px;">
      <p>Provision of advice is guided by legislative requirements to be provided in a Statement of Advice. Any and all comments regarding superannuation are not to be taken as advice rather than statement of factual information about the situation. The statement is not a recommendation to take any action unless that action is required by law. The client's personal situation has not been considered in providing the information. Any action to be taken in relation to the information provided should take into account the client's personal situation and consideration must be given as to whether action will be appropriate for the client's objectives and needs. Specific contribution amounts and SMSF product advice can only be provided under a Statement of Advice by a AFSL holder.</p>
    </div>
    <div class="body sign-off" style="top:186px;">
      <p>HartwellLane<br>Chartered Accountants</p>
    </div>
  </section>

  <section class="sheet" style="left:605px; top:72px;">
    <span class="running-head">2020 Tax Planning | Client Name Here</span>
    <div class="band"></div>
    <h2 class="page-title">Add Excel data...</h2>
  </section>

  <section class="sheet" style="left:780px; top:72px;">
    <span class="running-head">2020 Tax Planning | Client Name Here</span>
    <div class="band"></div>
    <div class="action-block" style="top:57px;">Items to Discuss</div>
    <div class="action-block" style="top:149px;">Action items to do now</div>
    <div class="action-block" style="top:242px;">Action items to see others about</div>
    <div class="action-block" style="top:342px;">Action items for after year end</div>
  </section>

  <!-- Row 2 -->
  <section class="sheet sheet--divider" style="left:77px; top:309px;">
    <span class="running-head">2020 Tax Planning | Client Name Here</span>
    <div class="band"></div>
    <h2 class="divider-title">Taxation Planning Stratagies<br>Main Taxation Plannings Strategies<br>Stategy</h2>
  </section>

  <section class="sheet" style="left:253px; top:309px;">
    <span class="running-head">2020 Tax Planning | Client Name Here</span>
    <div class="band"></div>
    <h2 class="page-title">Tax planning strategies</h2>
    <div class="body" style="top:62px;">
      <p>A more detailed list of potential tax planning strategies is as follows:</p>
      <h3 class="sub-title" style="margin-top:17px;">Main tax planning strategies</h3>
      <p style="margin-top:9px;">Strategy</p>
      <div class="strat" style="margin-top:38px;">
        <h3>Bring Forward Expenses</h3>
        <p>If possible, you should incur any business use expenses prior to 30 June. This way that expense will be included in the current tax year rather than next tax year, reducing your tax payable in this financial year.</p>
        <p class="note">Examples include: consumables, repairs, computer and office supplies.</p>
      </div>
      <div class="strat">
        <h3>Defer Income</h3>
        <p>If possible, you should defer issuing invoices in the last week or two until after 30 June 2019. This way that income will be included in the 2020 tax year rather than the 2019 tax year, deferring tax on the income for a year. Cash basis taxpayers should defer receipt of payment if possible.</p>
      </div>
      <div class="strat">
        <h3>Accounts Receivable</h3>
        <p>Under the small business tax concessions, the financial statements can be prepared on a cash basis so amounts receivable can be removed from the financial statements for tax purposes.</p>
      </div>
      <div class="strat">
        <h3>Accounts Payable</h3>
        <p>Under the small business tax concessions, the financial statements can be prepared on a cash basis so amounts payable can be removed from the financial statements for tax purposes.</p>
      </div>
      <div class="strat">
        <h3>Depreciation From Purchased Assets that Cost more than $30,000</h3>
        <p>A small business entity that purchases depreciating assets that cost more than</p>
        <ul>
          <li>$30,000 from 3 April 2019 – 30 June 2019</li>
          <li>$25,000 from 29 January 2019 – 2 April 2019</li>
          <li>$20,000 from 1 July 2018 – 28 January 2019</li>
        </ul>
      </div>
    </div>
  </section>

  <section class="sheet" style="left:429px; top:309px;">
    <span class="running-head">2020 Tax Planning | Client Name Here</span>
    <div class="band"></div>
    <h2 class="page-title">Main tax planning strategies (cont)</h2>
    <div class="body" style="top:64px;">
      <p>Will receive the following tax deductions from pooling the asset(s) in a small business asset pool:</p>
      <ul>
        <li>A 15% deduction in the 2019 tax year, regardless of when you purchased or acquired the asset during the year; and</li>
        <li>A 30% deduction each year after the first year.</li>
      </ul>
      <div class="strat">
        <h3>Bucket Company</h3>
        <p>If your business is trading through a trust and you have incurred higher than normal profits or the profits earned in your business are taxed at the highest marginal tax rate then a further tax planning strategy to consider is to set up a bucket company.</p>
      </div>
      <div class="strat">
        <h3>Instant Asset Write Off</h3>
        <p>You can immediately deduct the cost of a business asset if it costs (excluding GST) less than:</p>
        <ul>
          <li>$30,000 from 3 April 2019 – 30 June 2019</li>
          <li>$25,000 from 29 January 2019 – 2 April 2019</li>
          <li>$20,000 from 1 July 2018 – 28 January 2019</li>
        </ul>
        <p style="margin-top:6px;">This deduction can be used for each asset that costs less than $30,000, whether new or second hand.</p>
      </div>
      <div class="strat">
        <h3>Pay Employee Superannuation</h3>
        <p>To secure a tax deduction for your June quarter 2019 superannuation owing, we recommend that you pay this prior to 23 June 2019 to ensure that it has time to clear into the super funds prior to 30 June 2019. NOTE: This payment must clear your bank account prior to 30 June 2019 for it to be considered a tax deduction in the 2019 tax year.</p>
      </div>
      <div class="strat">
        <h3>One Year Lease</h3>
        <p>If you are considering purchasing plant and equipment in excess of $25,000 per item you could consider using a one year lease agreement to accelerate the tax deduction available. Providing the lease is structured correctly, the full amount of the lease payment is tax deductible in the year of payment.</p>
      </div>
      <div class="strat">
        <h3>Super – Optimise Tax Deductible Super Contributions</h3>
        <p>In the 2019 tax year, the concessional super contributions (gives you a tax deduction) cap is $25,000 for everyone.</p>
      </div>
    </div>
  </section>

  <section class="sheet" style="left:605px; top:309px;">
    <span class="running-head">2020 Tax Planning | Client Name Here</span>
    <div class="band"></div>
    <h2 class="page-title">Main tax planning strategies (cont)</h2>
    <div class="body" style="top:66px;">
      <p>Concessional super contributions include employer contributions (such as super guarantee and salary sacrifice contributions) and personal contributions.</p>
      <p>One strategy you could consider is to review your super contribution types and amounts to ensure your super contributions have been optimised.</p>
      <p>For example, if your employer contributions for the year are $15,000, you could choose to 'top up' your super to the $25,000 limit by making either a salary sacrifice contribution of $10,000 or a personal contribution of $10,000.</p>
      <div style="margin-top:4px;">
        <h4>Personal Super Contributions</h4>
        <p>Additionally, individuals under 75 years old can claim a tax deduction for personal super contributions (including those aged 65 to 74 who meet the work test).</p>
        <p>To satisfy the work test, a person must work at least 40 hours during a consecutive 30-day period each financial year in order for their fund to accept a personal super contribution for which they can claim a deduction.</p>
        <p>If you are interested in discussing this further, please contact our office and ask to speak to a licensed financial adviser.</p>
      </div>
      <div class="strat">
        <h3>Distribution to Children or Other Family Members Over 18</h3>
        <p>Children aged 18 at 30 June are taxed at adult tax rates and as such income can be split multiple ways rather than just between husband and wife. This can also apply to other family members such as parents or siblings if they don't have high incomes and are not in receipt of Centrelink allowances.</p>
      </div>
    </div>
  </section>

  <section class="sheet" style="left:780px; top:309px;">
    <span class="running-head">2020 Tax Planning | Client Name Here</span>
    <div class="band"></div>
    <h2 class="page-title">Other business tax planning strategies</h2>
    <div class="body" style="top:92px;">
      <div class="strat">
        <h3>Bonus Payments</h3>
        <p>Bonus payments to employees will be tax deductible to the employer in the 2019 year (even if the physical payments are not made until the following year), provided that the business is committed to the payments of quantified amounts prior to 30 June 2019.</p>
        <p>This will be evidenced by employment agreements and Resolutions of Directors / Trustees / Managers.</p>
      </div>
      <div class="strat">
        <h3>Business Travel Listing</h3>
        <p>Prepare listing of all business travel prior to 30 June 2019 for payment of travel allowances. This will increase your tax deductions, and reduce your tax payable.</p>
      </div>
      <div class="strat">
        <h3>Donations</h3>
        <p>Not only are donations to an organisation on the Deductible Gift Recipient register tax deductible, you will be supporting a very worthy cause. (The amount you wish to donate is at your discretion and the strategy cost listed to the right is to illustrate the potential tax savings).</p>
        <p>You will need to make your donation by 30 June 2019 to be able to claim a tax deduction for the 2019 year.</p>
      </div>
      <div class="strat">
        <h3>Home Office Costs</h3>
        <p>Keep a diary, like a log book, of the hours you work from home. Your diary evidence may then allow for an hourly rate claim for home office running costs.</p>
      </div>
      <div class="strat">
        <h3>Prepay Accounting Fees</h3>
        <p>Consider prepaying your accounting fees for the next year before 30 June 2019. You can claim an immediate tax deduction for such prepayments. (The strategy cost noted is only an estimate and was based upon your prior year tax returns to allow an indicative tax saving amount to be calculated).</p>
      </div>
    </div>
  </section>

  <section class="sheet" style="left:956px; top:309px;">
    <span class="running-head">2020 Tax Planning | Client Name Here</span>
    <div class="band"></div>
    <h2 class="page-title">Other business tax planning strategies (cont)</h2>
    <div class="body" style="top:92px;">
      <div class="strat">
        <h3>Review Trade Debtors &amp; Write off bad debts</h3>
        <p>Do you have any outstanding debtors that are unlikely to pay? If so, you should consider writing these off prior to 30 June 2019. The decision to write off bad debts should be documented prior to 30 June 2019 and your accounting system updated prior to 30 June 2019.</p>
      </div>
      <div class="strat">
        <h3>Spouse or Children Wage</h3>
        <p>Overall family tax can be reduced if income can be legitimately paid to a spouse or children over age 14 who has a lower tax rate. Wages can be paid to a spouse and can be treated as a tax deduction provided that the amount paid is reasonable for the duties performed. If the monthly wages are over $450, then employer superannuation of 9.5% will have to be paid on the wages amount. Workers compensation insurance and payroll tax may also apply to any wages paid.</p>
      </div>
      <div class="strat">
        <h3>Stock / Work in Progress Valuation</h3>
        <p>Stock and work in progress (WIP) are required to be valued at the end of 30 June 2019 at its cost, market selling price or replacement value. There is no obligation to use the same method for each item of stock – so it's worthwhile to consider the valuation method used for each stock item to potentially reduce your tax.</p>
        <p>The definition of each method is as follows:</p>
        <p><span class="term">Cost</span>: the cost of acquiring the trading stock / WIP plus any further costs in getting it into its existing condition or location.</p>
        <p><span class="term">Market Selling Value</span>: the current selling value of the item in your selling market.</p>
        <p><span class="term">Replacement Value</span>: the cost of replacing the item.</p>
        <p><span class="term">Obsolete Stock</span>: you may also elect to value an item of stock below any of the values above due to obsolescence or any other special circumstances.</p>
      </div>
      <div class="strat">
        <h3>Tax Audit Insurance</h3>
        <p>Audit insurance is a good way of ensuring you are not out of pocket in the event of an Australian Taxation Office (ATO) audit of your tax returns. The ATO are consistently increasing their audit activity through more and more data matching with third party institutions. If they find something that you have not declared and it takes time to resolve the issue, you can be left with a large accounting bill. For such a small tax-deductible premium you can have peace of mind should you ever be singled out.</p>
        <p>To claim a tax deduction for this in the 2019 year, you will need to pay your insurance premium before 30 June 2019.</p>
      </div>
    </div>
  </section>

</main>
</body>
</html>
```